Apartment Hotel
Zielgruppe
Apartment Hotel, verkauf von Hotelzimmer, bzw. Apartments. Für kurzreisende oder Langzeitaufenthalte, für Touristen , Geschäftsleuten, Firmen.
Wir stellen komplette 1 oder 2 Zimmerapartments mit Küche.
www.apartment-hotel-feldburg.de
Aufgabenstellung
modernes Logo , Briefpapier & Visitenkarten , Layout,
Platz für Name/Position: Hotelmanager

```html
<!DOCTYPE html>
<html lang="de">
<head>
<meta charset="utf-8">
<title>Feldburg Apartment Hotel – Geschäftsausstattung</title>
<link href="https://fonts.googleapis.com/css2?family=Questrial&display=swap" rel="stylesheet">
<style>
:root{
  --green:#a4c96a;
  --grey:#6f6f6f;
  --ink:#555;
  --paper:#fff;
  --line:#e6e6e6;
}
*{box-sizing:border-box;margin:0;padding:0}
html,body{width:1200px;height:900px;overflow:hidden;background:#fff}
body{position:relative;font-family:"Questrial",sans-serif;color:var(--ink)}
.sheet,.card{position:absolute;background:var(--paper);border:1px solid var(--line);box-shadow:8px 10px 14px rgba(0,0,0,.13);overflow:hidden}
.card--green{background:var(--green);border-color:#fff;border-width:2px}
.brand{position:absolute;left:0;right:0;text-align:center;color:var(--green)}
.brand__mark{display:block;margin:0 auto;background:var(--grey)}
.brand__name{display:block;letter-spacing:.04em;line-height:1}
.brand__tag{display:block;color:var(--grey);letter-spacing:.35em;line-height:1}
.card--green .brand,.card--green .brand__tag{color:#fff}
.card--green .brand__mark{background:var(--grey)}
.band-grey{position:absolute;left:0;right:0;background:var(--grey)}
.band-green{position:absolute;left:0;right:0;background:var(--green);color:#fff}
.contact-line{position:absolute;left:0;right:0;text-align:center;font-size:7.4px;letter-spacing:.06em;white-space:nowrap}
.contact-line .sep{color:var(--green);margin:0 4px}
.footer-col{position:absolute;font-size:8px;line-height:12px;letter-spacing:.06em;white-space:nowrap}
.small{position:absolute;font-size:5.4px;letter-spacing:.05em;white-space:nowrap;line-height:1}
</style>
</head>
<body>

<!-- Letterhead, back sheet -->
<div class="sheet" style="left:54px;top:104px;width:467px;height:658px">
  <div class="brand" style="top:10px">
    <span class="brand__mark" style="width:16px;height:16px;margin-bottom:10px"></span>
    <span class="brand__name" style="font-size:28px">FELDBURG</span>
  </div>
  <div class="band-grey" style="top:580px;height:9px"></div>
  <div class="band-green" style="top:596px;height:62px">
    <div class="footer-col" style="left:11px;top:6px">Bank-Name<br>Bankadresse 12<br>Kont-Nr. 002203030</div>
  </div>
</div>

<!-- Letterhead, front sheet -->
<div class="sheet" style="left:118px;top:186px;width:467px;height:657px">
  <div class="brand" style="top:9px">
    <span class="brand__mark" style="width:16px;height:16px;margin-bottom:10px"></span>
    <span class="brand__name" style="font-size:28px">FELDBURG</span>
    <span class="brand__tag" style="font-size:8px;margin-top:8px">APARTMENT HOTEL</span>
  </div>
  <div class="contact-line" style="top:98px">Ahornweg 12<span class="sep">|</span>04109 Leipzig<span class="sep">|</span>Tel.:+49 341 5520 4-10<span class="sep">|</span>Tel.:+49 341 5520 4-20<span class="sep">|</span>info@hotel-feldburg.de</div>
  <div class="band-grey" style="top:580px;height:9px"></div>
  <div class="band-green" style="top:595px;height:62px">
    <div class="footer-col" style="left:11px;top:7px">Bank-Name<br>Bankadresse 12<br>Kont-Nr. 002203030</div>
    <div class="footer-col" style="left:167px;top:8px">Tel.: 0043 11 11 111<br>Fax.: 0043 11 11 111<br>Mobil: 0000 11 11 1</div>
    <div class="footer-col" style="right:53px;top:8px;text-align:right">info@company.de<br>www.yourcompany.de<br>www.yourcompany.de</div>
  </div>
</div>

<!-- Business card, portrait, back -->
<div class="card" style="left:887px;top:83px;width:133px;height:217px">
  <div class="brand" style="top:13px">
    <span class="brand__mark" style="width:8px;height:8px;margin-bottom:6px"></span>
    <span class="brand__name" style="font-size:14px">FELDBURG</span>
    <span class="brand__tag" style="font-size:4px;margin-top:3px">APARTMENT HOTEL</span>
  </div>
  <div class="small" style="left:0;right:0;text-align:center;top:85px;font-size:6.5px">Muster Mustermann</div>
  <div class="small" style="left:0;right:0;text-align:center;top:94px;font-size:4.6px">Hotelmanager</div>
  <div class="small" style="left:0;right:0;text-align:center;top:110px;line-height:11px">Musterstrasse 1<br>111111 Musterort<br>Musterland</div>
  <div class="small" style="left:0;right:0;text-align:center;top:148px;font-size:6px;line-height:15px">Tel.: 0043 11 11<br>Fax.: 0043 11 11<br>Mobil.: 0043 11 11</div>
  <div class="band-grey" style="top:186px;height:3px"></div>
  <div class="band-green" style="top:193px;height:24px">
    <div class="small" style="left:6px;top:9px;color:#fff;font-size:5px">info@company.de</div>
  </div>
</div>

<!-- Business card, portrait, front -->
<div class="card card--green" style="left:954px;top:131px;width:133px;height:217px">
  <div class="brand" style="top:73px">
    <span class="brand__mark" style="width:9px;height:9px;margin-bottom:7px"></span>
    <span class="brand__name" style="font-size:17px">FELDBURG</span>
    <span class="brand__tag" style="font-size:4.6px;margin-top:4px">APARTMENT HOTEL</span>
  </div>
</div>

<!-- Business card, landscape, back -->
<div class="card" style="left:675px;top:469px;width:217px;height:133px">
  <div class="brand" style="top:8px;right:40px">
    <span class="brand__mark" style="width:7px;height:7px;margin-bottom:5px"></span>
    <span class="brand__name" style="font-size:12px">FELDBURG</span>
    <span class="brand__tag" style="font-size:3.4px;margin-top:3px">APARTMENT HOTEL</span>
  </div>
  <div class="small" style="left:12px;top:61px;line-height:12px">Musterstrasse 1<br>Musterland<br>111111 Musterort</div>
  <div class="small" style="left:122px;top:60px;width:90px;text-align:right;line-height:12px">Tel.: 0043 11 11<br>Fax.: 0043 11 11<br>Mobil.: 0043 11 11</div>
  <div class="band-grey" style="top:98px;height:3px"></div>
  <div class="band-green" style="top:104px;height:29px">
    <div class="small" style="left:7px;top:12px;color:#fff;font-size:7px">info@company.de</div>
    <div class="small" style="left:108px;top:12px;color:#fff;font-size:7px">www.company.de</div>
  </div>
</div>

<!-- Business card, landscape, front -->
<div class="card card--green" style="left:838px;top:501px;width:217px;height:133px">
  <div class="brand" style="top:38px">
    <span class="brand__mark" style="width:9px;height:9px;margin-bottom:7px"></span>
    <span class="brand__name" style="font-size:17px">FELDBURG</span>
    <span class="brand__tag" style="font-size:4.6px;margin-top:4px">APARTMENT HOTEL</span>
  </div>
</div>

<!-- Brand signature -->
<div class="brand" style="left:922px;right:36px;top:710px">
  <span class="brand__mark" style="width:26px;height:26px;margin-bottom:48px"></span>
  <span class="brand__name" style="font-size:50px">FELDBURG</span>
  <span class="brand__tag" style="font-size:15px;margin-top:12px">APARTMENT HOTEL</span>
</div>

</body>
</html>
```